WHERE LANTERNS GATHER

Where Lanterns Gather is the title of my book. The book is written to specifically address a major issue the world over which is the ability of think. Educational system in many parts of the world trains us to DO as supposed to Create. In the new world order, doing will always be inferior to thinking. The book is packed with methodologies and case studies. I need a unique design for the book.
Visual of the human brain as part of the creative element / rendition
Since the book is about creative thinking and innovation, I need a creative masterpiece that will be appealing to the eye on the shelf with a strong connection of curiosity & engagement. I personally am of the opinion that visual of the brain is quite off putting
AUTHOR: TOBENNA ADEKUNLE
PRINTED BY: MERIDIAN LEAF
BOOK SIZE: A5

Target Market(s)

Middle to Senior Level Managers in the Private Sector, Fresh Graduates, Entrepreneurs & SME Owners, Government

Font styles to use
Serif

Colors

Designer to choose colors to be used in the design.

Requirements
Must have
• On the front cover, in addition to the title, it should also have the pay off ''Discover & Discover & Unleash The Power Of Your Creative Mind
• Simple back cover design that allows for authors note etc to be very legible
• another must have is space for authors picture
• Front cover Star Burst (WARNING: this book will be difficult to lend)
Should not have
• Visual of the human brain as part of the creative element / rendition

```html
<!DOCTYPE html>
<html lang="en">
<head>
<meta charset="utf-8">
<title>Where Lanterns Gather – Book Cover</title>
<link rel="stylesheet" href="https://fonts.googleapis.com/css2?family=Josefin+Sans:wght@300;400;700&family=Oswald:wght@500&family=Open+Sans:wght@400&display=swap">
<style>
  :root {
    --backdrop: #fbf9d8;
    --paper: #ffffff;
    --ink: #1b3246;
    --band: #172c3d;
    --body-text: #2a3a48;
    --splash-pink: #e8507a;
    --splash-blue: #3aa6d8;
    --splash-yellow: #f2cf3a;
    --splash-teal: #47b9b0;
  }
  * { box-sizing: border-box; margin: 0; padding: 0; }
  html, body { width: 1200px; height: 1000px; overflow: hidden; }
  body {
    background: var(--backdrop);
    position: relative;
    font-family: "Josefin Sans", sans-serif;
    color: var(--ink);
  }

  .cover {
    position: absolute;
    background: var(--paper);
    overflow: hidden;
    box-shadow: 0 4px 18px rgba(0,0,0,0.12);
  }

  /* ---------- back cover ---------- */
  .back-cover { left: 150px; top: 170px; width: 420px; height: 650px; }
  .back-splash {
    position: absolute; left: 30px; top: 30px; width: 230px; height: 190px;
    border-radius: 45% 55% 50% 50%;
    background: radial-gradient(circle at 30% 40%, var(--splash-pink) 0%, transparent 45%),
                radial-gradient(circle at 70% 35%, var(--splash-blue) 0%, transparent 50%),
                radial-gradient(circle at 45% 75%, var(--splash-teal) 0%, transparent 45%),
                radial-gradient(circle at 60% 60%, var(--splash-yellow) 0%, transparent 35%);
    opacity: 0.8;
  }
  .author-photo-frame {
    position: absolute; left: 58px; top: 58px; width: 112px; height: 112px;
    border: 3px solid var(--paper);
    background: rgba(255,255,255,0.92);
    display: flex; align-items: center; justify-content: center; text-align: center;
    font-family: "Oswald", sans-serif; font-weight: 500; font-size: 19px; line-height: 1.15;
    color: var(--ink);
    outline: 3px solid var(--ink); outline-offset: -12px;
  }
  .back-title {
    position: absolute; left: 180px; top: 72px;
    font-weight: 700; line-height: 0.88; font-size: 40px; letter-spacing: -0.5px;
  }
  .back-title .small { font-size: 24px; display: block; }
  .back-body {
    position: absolute; left: 30px; right: 30px; top: 222px;
    font-family: "Open Sans", sans-serif; font-size: 10px; line-height: 1.5;
    color: var(--body-text); text-align: justify;
  }
  .back-body p + p { margin-top: 12px; }
  .back-footer {
    position: absolute; left: 40px; top: 585px;
    font-family: "Josefin Sans", sans-serif; font-size: 19px; line-height: 1.05;
  }
  .back-footer .strong { font-weight: 700; display: block; }
  .back-corner-splash {
    position: absolute; right: 0; bottom: 0; width: 110px; height: 90px;
    background: radial-gradient(circle at 70% 70%, var(--splash-pink) 0%, transparent 55%),
                radial-gradient(circle at 40% 80%, var(--splash-blue) 0%, transparent 45%),
                radial-gradient(circle at 80% 40%, var(--splash-yellow) 0%, transparent 35%);
    opacity: 0.75;
  }

  /* ---------- front cover ---------- */
  .front-cover { left: 610px; top: 150px; width: 440px; height: 690px; }
  .front-title {
    position: absolute; left: 26px; top: 34px;
    font-weight: 700; line-height: 0.9; font-size: 66px; letter-spacing: -1px;
  }
  .front-title .line { display: block; }
  .front-title .small { font-size: 46px; }
  .tagline {
    position: absolute; left: 28px; top: 275px;
    font-weight: 300; font-size: 19px; line-height: 1.25;
  }
  .tagline .emph { font-weight: 700; letter-spacing: 1.5px; display: block; font-size: 19px; }
  .head-art {
    position: absolute; left: 205px; top: 250px; width: 235px; height: 370px;
    background: linear-gradient(160deg, rgba(232,80,122,0.35) 0%, rgba(58,166,216,0.25) 25%, rgba(27,50,70,0.08) 55%, rgba(255,255,255,0) 100%);
    border-radius: 50% 40% 0 0;
  }
  .warning-burst {
    position: absolute; left: 24px; top: 380px; width: 175px; height: 175px;
    border-radius: 48% 52% 45% 55%;
    background: radial-gradient(circle at 30% 35%, var(--splash-blue) 0%, transparent 55%),
                radial-gradient(circle at 70% 60%, var(--splash-pink) 0%, transparent 50%),
                radial-gradient(circle at 50% 80%, var(--splash-yellow) 0%, transparent 45%),
                radial-gradient(circle at 50% 50%, var(--splash-teal) 0%, transparent 70%);
  }
  .warning-text {
    position: absolute; left: 54px; top: 414px; width: 115px; text-align: center;
    font-family: "Oswald", sans-serif; font-weight: 500; font-size: 13px; line-height: 1.15;
    color: var(--paper);
  }
  .warning-text .lead { font-size: 15px; display: block; }
  .warning-bulb {
    position: absolute; left: 58px; top: 398px;
  }
  .printer {
    position: absolute; left: 40px; top: 572px; text-align: center;
    font-family: "Oswald", sans-serif; font-weight: 500; font-size: 15px; line-height: 1.2;
  }
  .author-band {
    position: absolute; left: 0; right: 0; bottom: 0; height: 62px;
    background: var(--band); color: var(--paper);
    display: flex; align-items: center; justify-content: center;
    font-family: "Oswald", sans-serif; font-weight: 500; font-size: 32px; letter-spacing: 5px;
  }
</style>
</head>
<body>

  <section class="cover back-cover">
    <div class="back-splash" role="img" aria-label="Watercolour splash in pink, blue, teal and yellow"></div>
    <div class="author-photo-frame">PLACE<br>PICTURE<br>HERE</div>
    <h2 class="back-title"><span class="small">WHERE</span>LANTERNS<br><span class="small">GATHER</span></h2>
    <div class="back-body">
      <p>Lorem ipsum dolor sit amet, dicta consul usu in, ei animal officiis mandamus mei. Legere ridens meliore cum id, ex per ridens vivendo. Vix ad agam docendi omnesque. Salutatus sadipscing sea ea, cu modus mnesarchum pro, aeque facilisi sea ea. Ut pro causae eirmod, qui iriure tritani eloquentiam te. Te omnis malorum est, mel no nonumy libris deseruisse.</p>
      <p>Eum in ipsum alterum democritum, movet quodsi atomorum est cu. Eos te habeo habemus. Pri ad illud convenire. Te nullam dissentias est, ad sed quod unum. Elitr reprehendunt ad cum, est volumus detracto prodesset et, atqui populo postulant pro cu. Pro ut ceteros noluisse voluptaria.</p>
      <p>Eius tollit in pri. Urbanitas persecuti elaboraret cum ex, lorem quodsi legimus vel cu, ne ius eius primis labores. Eu nam sanctus ullamcorper conclusionemque. Mei sumo maiorum voluptatum ea.</p>
      <p>Interesset contentiones vim id, iudico legere contentiones per ex. Vel at nullam hendrerit, reque constituto voluptatum ei sit. Eum ad quod voluptua phaedrum. Saperet invidunt intellegat per at, an nam summo singulis, aliquid accusata euripidis ad usu. Ad has unum viris. Ut duo facer ubique deleniti, fastidii consequuntur et per. Ut vel vidisse indoctum assueverit, simul accumsan vivendum et nam.</p>
      <p>Ex possim propriae pro. Corpora expetenda similique at his, at habeo torquatos incorrupte cum, usu labore corrumpit ea. Qui ne elitr intellegat, nihil intellegat sadipscing at ius. Per ad nisl officiis.</p>
    </div>
    <div class="back-footer"><span class="strong">LOREM IPSUM</span>LOREM IPSUM</div>
    <div class="back-corner-splash" role="img" aria-label="Small watercolour splash with scattered triangles"></div>
  </section>

  <section class="cover front-cover">
    <h1 class="front-title">
      <span class="line small">WHERE</span>
      <span class="line">LANTERNS</span>
      <span class="line small">GATHER</span>
    </h1>
    <p class="tagline">DISCOVER &amp; UNLEASH<br>THE POWER OF YOUR<span class="emph">CREATIVE MIND</span></p>
    <div class="head-art" role="img" aria-label="Low-poly wireframe profile illustration with colourful watercolour burst"></div>
    <div class="warning-burst" role="img" aria-label="Watercolour burst behind a light bulb"></div>
    <svg class="warning-bulb" width="110" height="150" viewBox="0 0 110 150" aria-hidden="true">
      <path d="M55 4 C25 4 6 26 6 52 C6 72 20 84 30 96 C35 102 36 108 36 114 L74 114 C74 108 75 102 80 96 C90 84 104 72 104 52 C104 26 85 4 55 4 Z" fill="none" stroke="#ffffff" stroke-width="3"/>
      <line x1="38" y1="122" x2="72" y2="122" stroke="#ffffff" stroke-width="3"/>
      <line x1="40" y1="130" x2="70" y2="130" stroke="#ffffff" stroke-width="3"/>
      <path d="M44 138 L66 138 L60 146 L50 146 Z" fill="none" stroke="#ffffff" stroke-width="3"/>
    </svg>
    <p class="warning-text"><span class="lead">WARNING:</span>THIS BOOK<br>WILL BE<br>DIFFICULT<br>TO LEND</p>
    <p class="printer">PRINTED BY:<br>MERIDIAN LEAF</p>
    <div class="author-band">TOBENNA ADEKUNLE</div>
  </section>

</body>
</html>
```